Agriculture Business Need a Responsive Web Design

We need a Responsive Web Design for a Agriculture Business
We deliver agriculture data insight for farmers, media, salespersons and other that have an interrest in Agriculture.
Our products is a Velmorix - a application that helps people with insight on farms, and what this farms have deliveried of products. Products like Milk, grains, eggs, slaughtering of livestock, chicken, sheep and other slaughter of animals. Data about size of farms. We deliver stats about these farms. Compeare farms.

Target Market(s)

Agriculture businesses

Industry/Entity Type

Agriculture

Number of Pages Required

1 page

Font styles to use
Sans Serif

Requirements
Must have
• Responsive design. I.e the design shall be used on smartphones to desktop browsers. I think 2 columns on big screens that will collapse to 1 one small screens.

```html
<!DOCTYPE html>
<html lang="en">
<head>
<meta charset="utf-8">
<title>Velmorix – Agriculture Data</title>
<link rel="stylesheet" href="https://fonts.googleapis.com/css2?family=Raleway:wght@500;600;700;800&family=Open+Sans:wght@400;600;700&display=swap">
<style>
:root{
  --green:#7cb82f;
  --green-dark:#5e9a1c;
  --gold:#dfa83a;
  --sky:#5bb6d4;
  --cta:#70c1d8;
  --ink:#222;
  --text:#666;
  --muted:#999;
  --grey-bg:#f2f2f2;
  --footer:#2b2b2b;
  --footer-text:#bdbdbd;
  --white:#fff;
}
*{box-sizing:border-box;margin:0;padding:0}
html,body{width:1200px;height:2773px;overflow:hidden}
body{font-family:"Open Sans",Arial,sans-serif;color:var(--text);background:var(--white);position:relative}
h1,h2,h3,h4{font-family:"Raleway",Arial,sans-serif;color:var(--ink)}
.section{position:absolute;left:0;width:1200px}

/* header */
.site-header{top:0;height:89px;background:var(--white);border-top:4px solid var(--green)}
.brand{position:absolute;left:100px;top:18px;display:flex;align-items:center;gap:12px}
.brand-dot{width:46px;height:46px;border-radius:50%;background:var(--gold)}
.brand-name{font-family:"Raleway",sans-serif;font-weight:800;font-size:25px;color:var(--ink);letter-spacing:.5px}
.main-nav{position:absolute;left:392px;top:33px;width:556px;display:flex;justify-content:space-between;font-family:"Raleway",sans-serif;font-weight:700;font-size:13px;color:var(--ink);white-space:nowrap}
.main-nav .active{color:var(--green)}
.nav-search{position:absolute;left:972px;top:36px}
.nav-round{position:absolute;top:20px;width:46px;height:46px;border-radius:50%;border:2px solid var(--gold);display:flex;align-items:center;justify-content:center}
.nav-round.lock{left:998px}
.nav-round.edit{left:1052px;border-color:var(--green)}

/* hero */
.hero{top:89px;height:432px;background:linear-gradient(180deg,#3f5a2c 0%,#5d7a3c 40%,#8a8d5e 70%,#6b6a3e 100%)}
.hero h1{position:absolute;top:78px;width:100%;text-align:center;color:var(--white);font-size:38px;font-weight:800}
.hero p{position:absolute;top:134px;left:220px;width:760px;text-align:center;color:var(--white);font-size:15px;line-height:28px}
.signup{position:absolute;left:296px;top:232px;width:610px;height:76px;border:2px solid rgba(255,255,255,.7);border-radius:4px;display:flex;align-items:center;padding:0 20px;gap:0}
.signup .field{width:380px;height:52px;background:var(--white);font-size:12px;color:#555;display:flex;align-items:center;padding-left:22px}
.signup .btn{width:180px;height:52px;background:var(--green);color:var(--white);font-family:"Raleway",sans-serif;font-weight:800;font-size:17px;display:flex;align-items:center;justify-content:center}
.hero-dots{position:absolute;top:382px;left:560px;display:flex;gap:6px}
.hero-dots span{width:17px;height:17px;border-radius:50%;border:2px solid var(--white)}
.hero-dots .on{background:var(--green)}

/* welcome */
.welcome{top:521px;height:422px}
.section-title{font-size:26px;font-weight:800;text-align:center}
.welcome .section-title{margin-top:46px}
.welcome .lead{width:720px;margin:22px auto 0;text-align:center;font-size:14px;line-height:27px}
.audiences{position:absolute;top:167px;left:100px;width:1000px;display:flex;justify-content:space-between}
.audience{width:320px;text-align:center}
.audience-icon{width:122px;height:122px;border-radius:50%;margin:0 auto;display:flex;align-items:center;justify-content:center;border:4px solid var(--white);box-shadow:0 0 0 2px currentColor}
.audience h3{margin-top:26px;font-size:15px;font-weight:700}
.audience p{margin-top:10px;font-size:13.5px;line-height:23px}

/* stats */
.stats{top:943px;height:342px;background:var(--grey-bg)}
.stats h2{position:absolute;left:100px;top:60px;font-size:25px;font-weight:800}
.stats .copy{position:absolute;left:100px;top:110px;width:510px;font-size:12.5px;line-height:22px}
.stats .copy p+p{margin-top:14px}
.read-more{font-family:"Raleway",sans-serif;font-weight:700;font-size:13px;color:var(--green)}
.stats .read-more{position:absolute;left:100px;top:266px}
.pie{position:absolute;left:664px;top:28px;overflow:visible}
.pie text{font-family:"Open Sans",sans-serif;fill:var(--white);font-size:13px;text-anchor:middle}
.pie .val{font-weight:700;font-size:14px}

/* features */
.device{position:absolute;left:18px;top:46px;width:602px;height:333px;background:linear-gradient(180deg,#d8d8d8 0%,#bdbdbd 80%,#8c8c8c 100%);border-radius:14px 14px 4px 4px}
.features{top:1285px;height:388px}
.features h2{position:absolute;left:651px;top:76px;font-size:25px;font-weight:800}
.feature-list{position:absolute;left:651px;top:130px;list-style:none;font-size:12.5px}
.feature-list li{display:flex;align-items:center;gap:12px;height:37px}
.features .read-more{position:absolute;left:651px;top:329px}

/* testimonials */
.voices{top:1716px;height:296px;background:linear-gradient(120deg,#5a3a2a 0%,#6a5548 45%,#8a8f96 100%)}
.voice-card{position:absolute;top:54px;width:310px;height:160px;border:2px solid rgba(255,255,255,.85);border-radius:4px;background:rgba(0,0,0,.12);padding:16px 16px 0;color:var(--white)}
.voice-card.c1{left:98px}.voice-card.c2{left:444px}.voice-card.c3{left:791px}
.voice-head{display:flex;gap:12px;align-items:flex-start}
.avatar{width:46px;height:46px;background:#c9a47f;flex:none}
.voice-name{font-family:"Raleway",sans-serif;font-weight:700;font-size:16px}
.voice-handle{font-size:12.5px;color:#ddd}
.follow{margin-left:auto;border:1px solid var(--white);border-radius:3px;font-size:11px;padding:2px 8px}
.voice-card p{margin-top:12px;font-size:13px;line-height:20px}
.mention{color:var(--sky)}
.voice-meta{font-size:12px;margin-top:4px}
.voice-stats{font-size:12.5px;margin-top:8px;display:flex;gap:14px}
.stars{color:#f5b21a;font-size:12px;letter-spacing:1px}
.slider-arrow{position:absolute;top:130px;width:22px;height:36px}
.slider-arrow.l{left:32px}.slider-arrow.r{left:1146px}
.dots{position:absolute;top:248px;left:582px;display:flex;gap:4px}
.dots span{width:16px;height:16px;border-radius:50%;border:2px solid var(--white)}
.dots .on{background:var(--green)}

/* partners */
.partners{top:2012px;height:238px}
.partners .section-title{margin-top:52px;font-size:25px}
.partner-row{position:absolute;top:111px;left:181px;display:flex;gap:18px}
.partner{width:154px;height:74px;border:1px solid #ddd;display:flex;align-items:center;justify-content:center;font-family:"Open Sans",sans-serif;font-weight:600;font-size:19px;color:#2c4f8a}
.partners .slider-arrow{top:128px}
.partners .slider-arrow.l{left:96px}.partners .slider-arrow.r{left:1084px}

/* cta */
.cta{top:2250px;height:209px;background:var(--cta);text-align:center;color:var(--white)}
.cta h2{color:var(--white);font-size:26px;font-weight:700;margin-top:36px}
.cta p{font-size:14px;margin-top:10px}
.cta .btn{display:inline-flex;align-items:center;justify-content:center;margin-top:20px;width:180px;height:52px;background:var(--green);border-bottom:3px solid var(--green-dark);font-family:"Raleway",sans-serif;font-weight:800;font-size:16px}

/* footer */
.site-footer{top:2459px;height:314px;background:var(--footer);color:var(--footer-text)}
.site-footer .brand{left:100px;top:122px}
.site-footer .brand-name{color:var(--white)}
.foot-col{position:absolute;top:38px;font-size:12.5px;line-height:23px}
.foot-col h4{color:var(--white);font-size:15px;font-weight:700;margin-bottom:8px}
.foot-col ul{list-style:none}
.copyright{position:absolute;left:100px;top:270px;font-size:12px}
.socials{position:absolute;left:960px;top:260px;display:flex;gap:4px}
.socials span{width:34px;height:34px;border-radius:50%;border:2px solid var(--white)}
</style>
</head>
<body>

<header class="section site-header">
  <div class="brand"><span class="brand-dot"></span><span class="brand-name">VELMORIX</span></div>
  <nav class="main-nav">
    <span class="active">HOME</span><span>ABOUT US</span><span>PRODUCTS</span><span>FEATURES</span><span>BLOG</span><span>PRICING</span><span>CONTACT US</span>
  </nav>
  <svg class="nav-search" width="14" height="14" viewBox="0 0 14 14"><circle cx="6" cy="6" r="4.5" fill="none" stroke="#222" stroke-width="2"/><line x1="9.5" y1="9.5" x2="13" y2="13" stroke="#222" stroke-width="2"/></svg>
  <span class="nav-round lock"><svg width="18" height="20" viewBox="0 0 18 20"><path d="M4 9V6a5 5 0 0 1 10 0v3" fill="none" stroke="#dfa83a" stroke-width="2"/><rect x="2" y="9" width="14" height="10" rx="1" fill="#dfa83a"/></svg></span>
  <span class="nav-round edit"><svg width="18" height="18" viewBox="0 0 18 18"><path d="M3 15l1-4 9-9 3 3-9 9z" fill="none" stroke="#7cb82f" stroke-width="2"/></svg></span>
</header>

<section class="section hero" role="img" aria-label="Photo of a flock of sheep grazing on a green meadow in front of a forest">
  <h1>VELMORIX APPLICATION</h1>
  <p>A application that helps people with insight on farms, and what this farms have delivered of products. Products like Milk, grains, eggs, slaughtering of livestock, chicken, sheep and other slaughter of animals</p>
  <div class="signup"><span class="field">ENTER YOUR EMAIL ADDRESS</span><span class="btn">GET STARTED</span></div>
  <div class="hero-dots"><span class="on"></span><span></span><span></span><span></span></div>
</section>

<section class="section welcome">
  <h2 class="section-title">WELCOME TO VELMORIX</h2>
  <p class="lead">We deliver agriculture data insight for farmers, media and others who have an interest in Agriculture. We also provide Data about size of farms. We deliver stats about these farms. Compare farms etc.</p>
  <div class="audiences">
    <div class="audience">
      <div class="audience-icon" style="background:var(--green);color:var(--green)">
        <svg width="60" height="60" viewBox="0 0 60 60"><circle cx="24" cy="18" r="10" fill="#fff"/><path d="M6 54c0-14 8-22 18-22s18 8 18 22z" fill="#fff"/><path d="M46 20v34M46 26l-6-4M46 32l-6-4M46 38l-6-4M46 26l6-4M46 32l6-4M46 38l6-4" stroke="#fff" stroke-width="3" fill="none"/></svg>
      </div>
      <h3>FARMERS</h3>
      <p>We also provide Data about size of farms. We deliver stats about these farms.</p>
    </div>
    <div class="audience">
      <div class="audience-icon" style="background:var(--sky);color:var(--sky)">
        <svg width="60" height="60" viewBox="0 0 60 60"><g stroke="#fff" stroke-width="3"><line x1="30" y1="32" x2="30" y2="8"/><line x1="30" y1="32" x2="10" y2="44"/><line x1="30" y1="32" x2="50" y2="44"/><line x1="30" y1="32" x2="50" y2="20"/></g><circle cx="30" cy="32" r="9" fill="#fff"/><circle cx="30" cy="8" r="5" fill="#fff"/><circle cx="10" cy="44" r="5" fill="#fff"/><circle cx="50" cy="44" r="5" fill="#fff"/><circle cx="50" cy="20" r="4" fill="#fff"/></svg>
      </div>
      <h3>MEDIA</h3>
      <p>We also provide Data about size of farms. We deliver stats about these farms.</p>
    </div>
    <div class="audience">
      <div class="audience-icon" style="background:var(--gold);color:var(--gold)">
        <svg width="64" height="56" viewBox="0 0 64 56"><circle cx="32" cy="14" r="9" fill="#fff"/><path d="M16 48c0-12 7-20 16-20s16 8 16 20z" fill="#fff"/><circle cx="12" cy="20" r="7" fill="#fff"/><path d="M0 46c0-10 5-16 12-16 3 0 5 1 7 3-3 4-4 8-4 13z" fill="#fff"/><circle cx="52" cy="20" r="7" fill="#fff"/><path d="M64 46c0-10-5-16-12-16-3 0-5 1-7 3 3 4 4 8 4 13z" fill="#fff"/></svg>
      </div>
      <h3>INTERESTED PEOPLE</h3>
      <p>We also provide Data about size of farms. We deliver stats about these farms.</p>
    </div>
  </div>
</section>

<section class="section stats">
  <h2>VELMORIX STATISTICS</h2>
  <div class="copy">
    <p>At vero eos et accusamus et iusto odio dignissimos ducimus qui blanditiis praesentium voluptatum deleniti atque corrupti quos dolores et quas molestias excepturi sint occaecati cupiditate non provident, similique sunt.</p>
    <p>Culpa qui officia deserunt mollitia animi, id est laborum et dolorum fuga. Et harum quidem rerum facilis est et expedita distinctio.</p>
  </div>
  <span class="read-more">READ MORE &gt;&gt;</span>
  <svg class="pie" width="450" height="280" viewBox="0 0 450 280" aria-label="Pie chart of farm output by product">
    <defs>
      <g id="pie-side">
        <path d="M0 0L0 -220A220 220 0 0 1 168.5 -141.4Z" fill="#3a6c9c"/>
        <path d="M0 0L168.5 -141.4A220 220 0 0 1 219.2 19.2Z" fill="#9a3a45"/>
        <path d="M0 0L219.2 19.2A220 220 0 0 1 56.9 212.5Z" fill="#6f7f3a"/>
        <path d="M0 0L56.9 212.5A220 220 0 0 1 -126.2 180.2Z" fill="#4e3f7a"/>
        <path d="M0 0L-126.2 180.2A220 220 0 0 1 -219.2 19.2Z" fill="#8e3c8c"/>
        <path d="M0 0L-219.2 19.2A220 220 0 0 1 -141.4 -168.5Z" fill="#957a2c"/>
        <path d="M0 0L-141.4 -168.5A220 220 0 0 1 0 -220Z" fill="#2b8ea2"/>
      </g>
    </defs>
    <use href="#pie-side" transform="translate(225 140) scale(1 .45)"/>
    <use href="#pie-side" transform="translate(225 134) scale(1 .45)"/>
    <use href="#pie-side" transform="translate(225 128) scale(1 .45)"/>
    <use href="#pie-side" transform="translate(225 122) scale(1 .45)"/>
    <use href="#pie-side" transform="translate(225 116) scale(1 .45)"/>
    <use href="#pie-side" transform="translate(225 110) scale(1 .45)"/>
    <g transform="translate(225 105) scale(1 .45)">
      <path d="M0 0L0 -220A220 220 0 0 1 168.5 -141.4Z" fill="#4f8fcc"/>
      <path d="M0 0L168.5 -141.4A220 220 0 0 1 219.2 19.2Z" fill="#d0505c"/>
      <path d="M0 0L219.2 19.2A220 220 0 0 1 56.9 212.5Z" fill="#97b34e"/>
      <path d="M0 0L56.9 212.5A220 220 0 0 1 -126.2 180.2Z" fill="#7562ad"/>
      <path d="M0 0L-126.2 180.2A220 220 0 0 1 -219.2 19.2Z" fill="#c45ec4"/>
      <path d="M0 0L-219.2 19.2A220 220 0 0 1 -141.4 -168.5Z" fill="#d1ae4a"/>
      <path d="M0 0L-141.4 -168.5A220 220 0 0 1 0 -220Z" fill="#3fb6cc"/>
    </g>
    <text x="180" y="34">Milk</text><text class="val" x="180" y="51">$50,248</text>
    <text x="282" y="34">Grains</text><text class="val" x="282" y="51">$50,248</text>
    <text x="368" y="74">Eggs</text><text class="val" x="368" y="91">$50,248</text>
    <text x="350" y="124">other slaughter of</text><text x="350" y="139">animals</text><text class="val" x="350" y="156">$50,248</text>
    <text x="205" y="170">Sheep</text><text class="val" x="205" y="187">$50,248</text>
    <text x="110" y="140">Chicken</text><text class="val" x="110" y="157">$50,248</text>
    <text x="100" y="66">Slaughtering of</text><text x="100" y="81">livestock</text><text class="val" x="100" y="98">$50,248</text>
  </svg>
</section>

<section class="section features">
  <div class="device" role="img" aria-label="Laptop showing the application's developer view"></div>
  <h2>KEY FEATURES</h2>
  <ul class="feature-list">
    <li><svg width="14" height="14" viewBox="0 0 14 14"><circle cx="7" cy="7" r="7" fill="#dfa83a"/><path d="M4 7l2 2 4-4" stroke="#fff" stroke-width="1.8" fill="none"/></svg>On the other hand, we denounce with righteous indignation and dislike.</li>
    <li><svg width="14" height="14" viewBox="0 0 14 14"><circle cx="7" cy="7" r="7" fill="#dfa83a"/><path d="M4 7l2 2 4-4" stroke="#fff" stroke-width="1.8" fill="none"/></svg>At vero eos et accusamus et iusto odio dignissimos ducimus qui blanditiis.</li>
    <li><svg width="14" height="14" viewBox="0 0 14 14"><circle cx="7" cy="7" r="7" fill="#dfa83a"/><path d="M4 7l2 2 4-4" stroke="#fff" stroke-width="1.8" fill="none"/></svg>Certain circumstances and owing to the claims of duty or the oblig</li>
    <li><svg width="14" height="14" viewBox="0 0 14 14"><circle cx="7" cy="7" r="7" fill="#dfa83a"/><path d="M4 7l2 2 4-4" stroke="#fff" stroke-width="1.8" fill="none"/></svg>On the other hand, we denounce with righteous indignation and dislike.</li>
    <li><svg width="14" height="14" viewBox="0 0 14 14"><circle cx="7" cy="7" r="7" fill="#dfa83a"/><path d="M4 7l2 2 4-4" stroke="#fff" stroke-width="1.8" fill="none"/></svg>Nemo enim ipsam voluptatem quia voluptas sit aspernatur aut odit aut fugit,</li>
  </ul>
  <span class="read-more">READ MORE &gt;&gt;</span>
</section>

<section class="section voices" aria-label="Customer posts">
  <svg class="slider-arrow l" viewBox="0 0 22 36"><path d="M18 2L4 18l14 16" stroke="#fff" stroke-width="4" fill="none"/></svg>
  <svg class="slider-arrow r" viewBox="0 0 22 36"><path d="M4 2l14 16L4 34" stroke="#fff" stroke-width="4" fill="none"/></svg>
  <article class="voice-card c1">
    <div class="voice-head"><span class="avatar" role="img" aria-label="Profile photo"></span><div><div class="voice-name">Tom Harlan</div><div class="voice-handle">@harlan</div></div><span class="follow">Follow</span></div>
    <p>Neque porro <span class="mention">@fieldnews</span> est, qui dolorem ips quia dolor sit amet on</p>
    <div class="voice-meta">05:07 Pm - 12 Dec 2015</div>
    <div class="voice-stats"><span>↩ (0)</span><span>⇄ (2)</span><span>♥ (4)</span></div>
  </article>
  <article class="voice-card c2">
    <div class="voice-head"><span class="avatar" role="img" aria-label="Profile photo"></span><div><div class="voice-name">Mira Lund</div><div class="voice-handle">@miralund</div></div><span class="follow">Follow</span></div>
    <p>Neque porro <span class="mention">@fieldnews</span> est, qui dolorem ips quia dolor sit amet on</p>
    <div class="voice-meta">05:07 Pm - 12 Dec 2015</div>
    <div class="voice-stats"><span>↩ (0)</span><span>⇄ (2)</span><span>♥ (4)</span></div>
  </article>
  <article class="voice-card c3">
    <div class="voice-head"><span class="avatar" role="img" aria-label="Profile photo"></span><div><div class="voice-name">Elna Berg</div><div class="stars">★★★★★</div><div class="voice-handle">(7) &nbsp; (2)</div></div><span class="follow">Rate</span></div>
    <p>Neque porro est, qui dolorem ips quia dolor sit amet dolorem ips quia dt on</p>
    <div class="voice-meta">05:07 Pm - 12 Dec 2015</div>
  </article>
  <div class="dots"><span class="on"></span><span></span></div>
</section>

<section class="section partners">
  <h2 class="section-title">OVER 300 MILLION FOLLOWERS SERVED DAILY</h2>
  <svg class="slider-arrow l" viewBox="0 0 22 36"><path d="M16 8L6 18l10 10" stroke="#999" stroke-width="2.5" fill="none"/></svg>
  <div class="partner-row">
    <span class="partner">Brisko</span>
    <span class="partner">Consulna</span>
    <span class="partner">Tavenor</span>
    <span class="partner">UpFieldGo</span>
    <span class="partner">Growlearn</span>
  </div>
  <svg class="slider-arrow r" viewBox="0 0 22 36"><path d="M6 8l10 10L6 28" stroke="#999" stroke-width="2.5" fill="none"/></svg>
</section>

<section class="section cta">
  <h2>SCHEDULE A DEMO TO SEE OUR FULL APPLICATION IN ACTION</h2>
  <p>At vero eos et accusamus et iusto odio dignissimos ducimus qui blanditiis praesentium voluptatum corrupti</p>
  <span class="btn">GET STARTED</span>
</section>

<footer class="section site-footer">
  <div class="brand"><span class="brand-dot"></span><span class="brand-name">VELMORIX</span></div>
  <div class="foot-col" style="left:346px"><h4>About us</h4><ul><li>Our Story</li><li>Team</li><li>Newsletters</li><li>Contact</li><li>Jobs</li><li>Help Us Grow</li></ul></div>
  <div class="foot-col" style="left:471px"><h4>Products</h4><ul><li>Fieldwork Projects</li><li>Fieldwork Desk</li><li>Fieldwork Chat</li></ul></div>
  <div class="foot-col" style="left:632px"><h4>Links</h4><ul><li>Desktop Timer App</li><li>Cloud Suite for Business</li><li>Tablet App</li><li>Phone App</li><li>Mobile App</li></ul></div>
  <div class="foot-col" style="left:826px"><h4>Resources</h4><ul><li>Roadmap &amp; Updates</li><li>Security</li><li>Privacy Policy</li><li>Terms of Service</li><li>Webinars</li><li>Free for Startups</li></ul></div>
  <div class="foot-col" style="left:1000px"><h4>Legal</h4><ul><li>Certified Trainers</li><li>Fieldwork</li><li>Developer Zone</li><li>Referral Program</li><li>Refund Policy</li><li>Login</li></ul></div>
  <p class="copyright">Copyrights © 2016, Velmorix. All rights reserved.</p>
  <div class="socials"><span></span><span></span><span></span><span></span></div>
</footer>

</body>
</html>
```